distributor of aftermarket auto electrical components

I am after business card design for my new company called
Summit Vehicle Supplies (SVS as the acronym). I will supplying automotive wiring components, basically from battery to headlight. I will be aiming to sell in the 4wd scene and to auto electricians. i am not worried which colours are used though i would like it to be dynamic.
Updates

sorry guys, i have add a mobile and e-mail address that will need to on there as well. Sorry for theĀ inconvenience.

sorry guys i had erred on my spelling with my e-mail. i have now fixed it in the brief

Target Market(s)

4wd industry, custom cars, RV, auto electricians

Industry/Entity Type

Electrical

Requirements
Must have
• Company Name
ABN number: 71 306 548 290
Director: Derek Holloway
M 0432 718 946
E dhollo@fernwire.com.au

```html
<!DOCTYPE html>
<html lang="en">
<head>
<meta charset="utf-8">
<title>Summit Vehicle Supplies – Business Card</title>
<link rel="stylesheet" href="https://fonts.googleapis.com/css2?family=Arimo:wght@400;700&display=swap">
<style>
  :root {
    --navy: #124a86;
    --navy-deep: #0b3566;
    --navy-light: #1f63a8;
    --orange: #f7ac33;
    --silver: #c9c9cb;
    --silver-dark: #5a5a5c;
    --ink-grey: #555a60;
    --paper: #ffffff;
    --stage: #ffffff;
  }
  html, body {
    margin: 0;
    padding: 0;
    width: 1200px;
    height: 901px;
    overflow: hidden;
    background: var(--stage);
    font-family: "Arimo", Arial, sans-serif;
  }
  .card {
    position: absolute;
    left: 271px;
    width: 640px;
    height: 367px;
    overflow: hidden;
    box-shadow: 3px 5px 8px rgba(0,0,0,0.35);
  }
  .card--front { top: 53px; }
  .card--back { top: 504px; }
  .card__bg {
    position: absolute;
    inset: 0;
    width: 640px;
    height: 367px;
  }
  .brand {
    position: absolute;
    text-align: center;
    font-weight: 700;
  }
  .brand__acronym {
    display: flex;
    align-items: center;
    justify-content: center;
    gap: 12px;
    font-size: 68px;
    letter-spacing: 6px;
    line-height: 1;
  }
  .brand__dot {
    width: 14px;
    height: 14px;
    border-radius: 50%;
    background: var(--orange);
  }
  .brand__name {
    font-size: 22px;
    margin-top: 14px;
    letter-spacing: 0.2px;
  }
  .card--front .brand {
    left: 0;
    right: 0;
    top: 120px;
    color: var(--paper);
  }
  .card--back .brand {
    left: 295px;
    width: 330px;
    top: 62px;
    color: var(--navy);
  }
  .card--back .brand__acronym { font-size: 58px; }
  .card--back .brand__name { font-size: 19px; margin-top: 10px; }
  .person {
    position: absolute;
    left: 77px;
    top: 116px;
  }
  .person__name {
    font-size: 21px;
    font-weight: 700;
    color: var(--navy);
  }
  .person__role {
    font-size: 16px;
    color: var(--ink-grey);
    margin-top: 3px;
  }
  .contact {
    position: absolute;
    left: 36px;
    top: 300px;
    color: var(--paper);
    font-size: 17px;
    line-height: 24px;
  }
  .contact__row {
    display: flex;
    align-items: center;
    gap: 8px;
  }
  .contact__icon {
    width: 14px;
    height: 14px;
    flex: none;
  }
  .abn {
    position: absolute;
    right: 33px;
    top: 300px;
    color: var(--paper);
    font-size: 17px;
    line-height: 24px;
  }
</style>
</head>
<body>

  <section class="card card--front" aria-label="Business card front">
    <svg class="card__bg" viewBox="0 0 640 367" aria-hidden="true">
      <defs>
        <radialGradient id="front-blue" cx="50%" cy="45%" r="65%">
          <stop offset="0" stop-color="var(--navy-light)"/>
          <stop offset="1" stop-color="var(--navy-deep)"/>
        </radialGradient>
        <linearGradient id="front-silver" x1="0" y1="0" x2="1" y2="1">
          <stop offset="0" stop-color="#8d8d90"/>
          <stop offset="0.5" stop-color="#e6e6e8"/>
          <stop offset="1" stop-color="#9a9a9d"/>
        </linearGradient>
      </defs>
      <rect width="640" height="367" fill="url(#front-blue)"/>
      <path d="M0,0 H185 Q70,45 0,150 Z" fill="url(#front-silver)"/>
      <path d="M185,0 Q70,45 0,150" fill="none" stroke="var(--silver-dark)" stroke-width="9"/>
      <path d="M640,367 H455 Q575,325 640,210 Z" fill="url(#front-silver)"/>
      <path d="M455,367 Q575,325 640,210" fill="none" stroke="var(--silver-dark)" stroke-width="9"/>
    </svg>
    <div class="brand">
      <div class="brand__acronym">SVS<span class="brand__dot"></span></div>
      <div class="brand__name">Summit Vehicle Supplies</div>
    </div>
  </section>

  <section class="card card--back" aria-label="Business card back">
    <svg class="card__bg" viewBox="0 0 640 367" aria-hidden="true">
      <defs>
        <radialGradient id="back-blue" cx="40%" cy="90%" r="80%">
          <stop offset="0" stop-color="var(--navy-light)"/>
          <stop offset="1" stop-color="var(--navy-deep)"/>
        </radialGradient>
        <linearGradient id="back-silver" x1="0" y1="0" x2="1" y2="0">
          <stop offset="0" stop-color="#7c7c80"/>
          <stop offset="0.5" stop-color="#d8d8da"/>
          <stop offset="1" stop-color="#6e6e72"/>
        </linearGradient>
      </defs>
      <rect width="640" height="367" fill="url(#back-blue)"/>
      <path d="M28,0 H640 V200 C540,275 400,320 260,318 C90,315 -8,200 28,0 Z" fill="url(#back-silver)"/>
      <path d="M56,0 H640 V185 C540,255 400,298 270,297 C120,295 22,205 56,0 Z" fill="var(--paper)"/>
      <path d="M235,306 C420,300 565,258 640,203 V226 C560,282 420,312 235,306 Z" fill="var(--orange)"/>
    </svg>

    <div class="brand">
      <div class="brand__acronym">SVS<span class="brand__dot"></span></div>
      <div class="brand__name">Summit Vehicle Supplies</div>
    </div>

    <div class="person">
      <div class="person__name">Derek Holloway</div>
      <div class="person__role">Director</div>
    </div>

    <div class="contact">
      <div class="contact__row">
        <svg class="contact__icon" viewBox="0 0 14 14" aria-hidden="true">
          <rect x="3" y="0.5" width="8" height="13" rx="1.5" fill="var(--orange)"/>
          <rect x="4.5" y="2" width="5" height="7" fill="var(--navy)"/>
        </svg>
        <span>0432 718 946</span>
      </div>
      <div class="contact__row">
        <svg class="contact__icon" viewBox="0 0 14 14" aria-hidden="true">
          <rect x="0.5" y="2.5" width="13" height="9" fill="var(--orange)"/>
          <path d="M0.5,2.5 L7,8 L13.5,2.5" fill="none" stroke="var(--navy)" stroke-width="1.2"/>
        </svg>
        <span>dhollo@fernwire.com.au</span>
      </div>
    </div>

    <div class="abn">ABN number: 71 306 548 290</div>
  </section>

</body>
</html>
```